TORLO Facility Services ball field sign

Hello all!
I have bought a 4x6 sign space at our local Brindle Green baseball field. This sign space will be used to display a sign for TORLO Facility Services. The color, font and logos are located in the files attached. May accept the following on the sign: “HVAC · Refrigeration · Plumbing · Electrical · Commercial Cooking Equipment”. I would maybe like to see some designs that match our van rap style. Another slogan we use sometimes is “ One Call. Every Trade. Every Time.” QR Code could be used to schedule service.

Target Market(s)

Commercial Customers

Industry/Entity Type

Commercial Facility Services

Requirements
Must have
• Phone: 512.683.2097; WEB: www.TORLOFS-example.com
Should not have
• Do not mention anything related to county or park on the sign

```html
<!DOCTYPE html>
<html lang="en">
<head>
<meta charset="utf-8">
<title>TORLO Facility Services – Ball Field Sign Concepts</title>
<link rel="stylesheet" href="https://fonts.googleapis.com/css2?family=Oswald:wght@600&family=Poppins:wght@700;800&display=swap">
<style>
  :root {
    --brand-blue: #1047a0;
    --white: #ffffff;
    --backdrop: #444444;
    --steel-light: #d3d6d6;
    --steel-mid: #a4b5bb;
    --font-tag: "Oswald", "Arial Narrow", sans-serif;
    --font-main: "Poppins", "Arial", sans-serif;
  }
  * { margin: 0; padding: 0; box-sizing: border-box; }
  html, body { width: 1200px; height: 908px; overflow: hidden; background: var(--backdrop); }
  .board { position: relative; width: 1200px; height: 908px; }
  .sign { position: absolute; width: 455px; height: 303px; overflow: hidden; background: var(--white); }
  .sign svg.backing { position: absolute; inset: 0; }
  .sign-arc-top { left: 126px; top: 134px; }
  .sign-diagonal { left: 619px; top: 134px; }
  .sign-arc-bottom { left: 126px; top: 475px; }
  .sign-band { left: 619px; top: 475px; }
  .txt { position: absolute; white-space: nowrap; line-height: 1; }
  .center { left: 0; right: 0; text-align: center; }
  .wordmark { font-family: var(--font-main); font-weight: 700; font-size: 36px; letter-spacing: 1px; color: var(--brand-blue); }
  .wordmark.on-blue { color: var(--white); }
  .tagline { font-family: var(--font-tag); font-weight: 600; font-size: 26px; color: var(--white); }
  .tagline.on-white { color: var(--brand-blue); }
  .phone { font-family: var(--font-main); font-weight: 700; font-size: 50px; color: var(--white); letter-spacing: -0.5px; }
  .phone.on-white { color: var(--brand-blue); }
  .web { font-family: var(--font-main); font-weight: 700; font-size: 18px; color: var(--white); }
  .web.on-white { color: var(--brand-blue); }
  .stack-tagline { right: 22px; text-align: right; font-family: var(--font-tag); font-weight: 600; font-size: 38px; line-height: 47px; color: var(--white); }
  .stack-phone { right: 22px; font-family: var(--font-tag); font-weight: 600; font-size: 42px; color: var(--white); }
  .stack-web { right: 22px; font-family: var(--font-main); font-weight: 700; font-size: 16px; color: var(--white); }
  .caps-headline { left: 22px; font-family: var(--font-main); font-weight: 700; font-size: 33px; line-height: 48px; color: var(--brand-blue); }
  .band-phone { left: 0; right: 0; text-align: center; font-family: var(--font-main); font-weight: 800; font-size: 55px; color: var(--white); letter-spacing: -0.5px; }
  .band-web { left: 29px; font-family: var(--font-main); font-weight: 700; font-size: 20px; color: var(--brand-blue); }
</style>
</head>
<body>
<main class="board">

  <section class="sign sign-arc-top">
    <svg class="backing" width="455" height="303" viewBox="0 0 455 303">
      <defs>
        <linearGradient id="steelSweepA" x1="0" x2="1" y1="0" y2="0">
          <stop offset="0" stop-color="var(--steel-mid)"/>
          <stop offset="0.5" stop-color="var(--steel-light)"/>
          <stop offset="1" stop-color="var(--steel-mid)"/>
        </linearGradient>
      </defs>
      <path d="M0 83 Q227.5 135 455 83 V303 H0 Z" fill="url(#steelSweepA)"/>
      <path d="M0 88 Q227.5 178 455 88 V303 H0 Z" fill="var(--brand-blue)"/>
    </svg>
    <div class="txt center wordmark" style="top:38px;">TORLO</div>
    <div class="txt center tagline" style="top:150px;">One Call. Every Trade. Every Time.</div>
    <div class="txt center phone" style="top:196px;">512.683.2097</div>
    <div class="txt center web" style="top:264px;">www.TORLOFS-example.com</div>
  </section>

  <section class="sign sign-diagonal">
    <svg class="backing" width="455" height="303" viewBox="0 0 455 303">
      <defs>
        <linearGradient id="steelFold" x1="0" x2="1" y1="1" y2="0">
          <stop offset="0" stop-color="var(--steel-mid)"/>
          <stop offset="0.6" stop-color="var(--steel-light)"/>
          <stop offset="1" stop-color="var(--steel-mid)"/>
        </linearGradient>
      </defs>
      <path d="M0 303 L184 103 L60 303 Z" fill="url(#steelFold)"/>
      <path d="M184 103 L117 303 L60 303 Z" fill="var(--steel-mid)"/>
      <path d="M219 0 H455 V303 H117 Z" fill="var(--brand-blue)"/>
    </svg>
    <div class="txt wordmark" style="left:28px; top:38px;">TORLO</div>
    <div class="txt stack-tagline" style="top:22px;">One Call.<br>Every Trade.<br>Every Time.</div>
    <div class="txt stack-phone" style="top:190px;">512.683.2097</div>
    <div class="txt stack-web" style="top:256px;">www.TORLOFS-example.com</div>
  </section>

  <section class="sign sign-arc-bottom">
    <svg class="backing" width="455" height="303" viewBox="0 0 455 303">
      <defs>
        <linearGradient id="steelSweepB" x1="0" x2="1" y1="0" y2="0">
          <stop offset="0" stop-color="var(--steel-mid)"/>
          <stop offset="0.5" stop-color="var(--steel-light)"/>
          <stop offset="1" stop-color="var(--steel-mid)"/>
        </linearGradient>
      </defs>
      <path d="M0 82 Q227.5 176 455 82 V0 H0 Z" fill="url(#steelSweepB)"/>
      <path d="M0 82 Q227.5 130 455 82 V0 H0 Z" fill="var(--brand-blue)"/>
    </svg>
    <div class="txt center wordmark on-blue" style="top:32px;">TORLO</div>
    <div class="txt center tagline on-white" style="top:146px;">One Call. Every Trade. Every Time.</div>
    <div class="txt center phone on-white" style="top:191px;">512.683.2097</div>
    <div class="txt center web on-white" style="top:261px;">www.TORLOFS-example.com</div>
  </section>

  <section class="sign sign-band">
    <svg class="backing" width="455" height="303" viewBox="0 0 455 303">
      <rect x="0" y="167" width="455" height="82" fill="var(--brand-blue)"/>
    </svg>
    <div class="txt caps-headline" style="top:16px;">ONE CALL.<br>EVERY TRADE.<br>EVERY TIME.</div>
    <div class="txt wordmark" style="left:324px; top:26px; font-size:32px;">TORLO</div>
    <div class="txt band-phone" style="top:180px;">512.683.2097</div>
    <div class="txt band-web" style="top:264px;">www.TORLOFS-example.com</div>
  </section>

</main>
</body>
</html>
```